Amber Lantern Cafe Business Card

We need a business card design for a new European Cafe. Main menu will be coffee and deserts.

Requirements
Must have
• Logo - 1 of the attached versions
Address - TBA (you can use 487 Morrow Ave Unit 9 for now)
Phone - TBA (you can use 555-238-4176 for now)

```html
<!DOCTYPE html>
<html lang="en">
<head>
<meta charset="utf-8">
<title>Amber Lantern Cafe – Business Card</title>
<link href="https://fonts.googleapis.com/css2?family=Cormorant+Garamond:wght@500&family=Arimo:wght@400&display=swap" rel="stylesheet">
<style>
  :root {
    --stage: #efeceb;
    --wine-light: #8c2244;
    --wine-mid: #6a1530;
    --wine-dark: #420b1d;
    --card-white: #ffffff;
    --ink-wine: #5a1a2a;
    --ink-text: #3a2a2e;
    --rule: #6a4a52;
    --on-wine: #ffffff;
  }
  * { box-sizing: border-box; margin: 0; padding: 0; }
  html, body {
    width: 1200px;
    height: 424px;
    overflow: hidden;
    background: var(--stage);
  }
  .canvas {
    position: relative;
    width: 1200px;
    height: 424px;
    display: flex;
    align-items: center;
    justify-content: center;
    gap: 60px;
  }
  .card {
    position: relative;
    width: 500px;
    height: 300px;
    box-shadow: 0 2px 10px rgba(0,0,0,0.18);
  }
  .card--front {
    background:
      repeating-linear-gradient(90deg, rgba(255,255,255,0.025) 0 6px, rgba(0,0,0,0.025) 6px 12px),
      radial-gradient(ellipse at 55% 40%, var(--wine-light) 0%, var(--wine-mid) 45%, var(--wine-dark) 100%);
    display: flex;
    flex-direction: column;
    align-items: center;
    justify-content: center;
    color: var(--on-wine);
  }
  .card--back {
    background: var(--card-white);
    color: var(--ink-wine);
  }
  .brand {
    font-family: "Cormorant Garamond", "Times New Roman", serif;
    font-weight: 500;
    text-align: center;
    line-height: 1.15;
  }
  .brand-dot {
    display: block;
    border-radius: 50%;
    margin: 0 auto;
  }
  .card--front .brand-dot {
    width: 34px;
    height: 34px;
    border: 2px solid var(--on-wine);
    margin-bottom: 18px;
  }
  .card--front .brand-name { font-size: 30px; }
  .card--front .brand-sub { font-size: 24px; margin-top: 6px; }

  .card--back .brand-block {
    position: absolute;
    top: 44px;
    left: 0;
    right: 0;
  }
  .card--back .brand-dot {
    width: 22px;
    height: 22px;
    border: 1.5px solid var(--ink-wine);
    margin-bottom: 10px;
  }
  .card--back .brand-name { font-size: 22px; }
  .card--back .brand-sub { font-size: 18px; margin-top: 2px; }

  .contact {
    position: absolute;
    top: 178px;
    left: 0;
    right: 0;
    display: flex;
    justify-content: center;
    font-family: "Arimo", Arial, sans-serif;
    font-size: 11.5px;
    line-height: 1.45;
    color: var(--ink-text);
  }
  .contact-col { width: 150px; }
  .contact-col--left { text-align: left; padding-right: 12px; }
  .contact-col--right { padding-left: 8px; width: 170px; }
  .contact-rule {
    width: 1px;
    height: 84px;
    margin-top: -4px;
    background: var(--rule);
  }
</style>
</head>
<body>
  <main class="canvas">
    <section class="card card--front" aria-label="Card front">
      <div class="brand">
        <span class="brand-dot" aria-hidden="true"></span>
        <div class="brand-name">Amber Lantern</div>
        <div class="brand-sub">Cafe</div>
      </div>
    </section>

    <section class="card card--back" aria-label="Card back">
      <div class="brand brand-block">
        <span class="brand-dot" aria-hidden="true"></span>
        <div class="brand-name">Amber Lantern</div>
        <div class="brand-sub">Cafe</div>
      </div>
      <div class="contact">
        <div class="contact-col contact-col--left">
          <p>Add - 487 Morrow Ave</p>
          <p>Add - Unit 9</p>
          <p>Add - Open daily 7-7</p>
        </div>
        <div class="contact-rule" aria-hidden="true"></div>
        <div class="contact-col contact-col--right">
          <p>http://www.amberlantern.co</p>
          <p>E-mail:hello@amberlantern.co</p>
          <p>Phone -&nbsp; 555-238-4176</p>
        </div>
      </div>
    </section>
  </main>
</body>
</html>
```